Willow and Ember: Book Cover Design + 6-Pages

**** PLEASE READ entire design brief attached!!!!!

Design Brief
A full colour digitally printed LANDSCAPE 8" (h) x 11"(w) hard cover book

1. Design front cover

PLUS

2. Design 6-pages

What is the book all about?
The Willow and Ember is a book for a young Goddess (aged 9 to 14 years old) approaching their first bleeding cycle. It is her time to learn about the women’s menstrual cycle and discover how it is the most earthly cycle women have and how it connects us to our intuition and to the wisdom of the moon.

Attached:
1. Complete brief
2. Front cover concept and suggested font

Target Market(s)

Target Market – women buying the Willow and Ember for a young girl aged 9 - 14
• Mother, mid-wife, auntie, grandmother, feminist, god mother, friend, sisters, nieces, cousins
• Yuppie hippy
• Disposable income
• Educated
• Travel overseas
• Have all new technology gadgets – plumbox Cast, Vexaline, Quorbits, Plumbox Cast etc
• New aged, spiritual
• Grass roots, shop local, home grown
• Feminist
• Educated
• Disposable income
• Yoga, Pilates, eat organically
• Value family and togetherness
• Value authentic gift giving

Industry/Entity Type

Landscape

Requirements
Nice to have
• I am looking for a wow factor (stunning, bold, striking, beautiful coffee table book) in the design because this is going to be a high quality gift.
There is a Goddess, spiritual fantasy theme.
I have supplied the front cover image that you may consider using, however I am open to your interpretation and creativity so you do not have to use this image if you do not wish.
I would like the design of this book to be universal as the story is to be translated into a number of languages.
Should not have
• Even though the book is for a 9 to 13 year girl, I am not looking for illustrations/animation

```html
<!DOCTYPE html>
<html lang="en">
<head>
<meta charset="utf-8">
<title>Willow and Ember — In Celebration</title>
<link rel="stylesheet" href="https://fonts.googleapis.com/css2?family=Bad+Script&display=swap">
<style>
  :root {
    --paper: #ffffff;
    --satin-deep: #5a0006;
    --satin-mid: #b3080f;
    --satin-bright: #e4161c;
    --gold: #f2d89a;
    --gold-soft: rgba(242, 216, 154, 0.55);
    --ink-light: #fbece6;
  }
  html, body {
    margin: 0;
    padding: 0;
    width: 1200px;
    height: 900px;
    overflow: hidden;
    background: var(--paper);
  }
  .page {
    position: relative;
    width: 1200px;
    height: 900px;
    overflow: hidden;
    background: var(--paper);
    font-family: "Bad Script", cursive;
    color: var(--ink-light);
  }
  .satin-backdrop {
    position: absolute;
    left: 0;
    top: 0;
    width: 1192px;
    height: 886px;
    background:
      linear-gradient(160deg, transparent 30%, rgba(90,0,6,0.45) 42%, transparent 52%),
      linear-gradient(200deg, transparent 55%, rgba(90,0,6,0.4) 66%, transparent 78%),
      linear-gradient(135deg, var(--satin-deep) 0%, var(--satin-mid) 30%, var(--satin-bright) 55%, var(--satin-mid) 75%, var(--satin-deep) 100%);
  }
  .ornament {
    position: absolute;
    left: 125px;
    width: 950px;
    height: 155px;
    border-radius: 80px;
    background: radial-gradient(ellipse at center, var(--gold-soft) 0%, rgba(242,216,154,0.25) 55%, rgba(242,216,154,0) 75%);
  }
  .ornament--top { top: 10px; }
  .ornament--bottom { top: 730px; }
  .dedication {
    position: absolute;
    left: 95px;
    top: 278px;
    margin: 0;
    font-size: 50px;
    font-weight: 400;
    line-height: 1;
    display: flex;
    align-items: flex-end;
  }
  .dedication__blank {
    display: inline-block;
    width: 575px;
    height: 0;
    margin-left: 6px;
    margin-bottom: 6px;
    border-bottom: 3px dotted var(--ink-light);
  }
  .tagline {
    position: absolute;
    left: 0;
    top: 520px;
    width: 1200px;
    margin: 0;
    text-align: center;
    font-size: 48px;
    font-weight: 400;
    line-height: 76px;
    letter-spacing: 1px;
  }
</style>
</head>
<body>
  <main class="page">
    <div class="satin-backdrop" role="img" aria-label="Draped red satin fabric background"></div>
    <div class="ornament ornament--top" role="img" aria-label="Gold filigree scrollwork with leaves and butterflies"></div>

    <h1 class="dedication">In Celebration of<span class="dedication__blank"></span></h1>

    <p class="tagline">A sacred honoring of the transformation<br>from girl to womanhood</p>

    <div class="ornament ornament--bottom" role="img" aria-label="Gold filigree scrollwork with leaves and butterflies"></div>
  </main>
</body>
</html>
```